New Business Card Design Project

I would like a business card to match my truck wrap and logo. I would like the font to match my existing business card please.

Industry/Entity Type

Painter

Contact Information for Business Card

Rodrigo Venter 801-437-2910 Ventercoatings.utah@brushmail.net
SERVICES - Custom Paint & Stain, Interior & Exterior, Epoxy Coatings / Garage Floors, Cabinet Refinishing, Log Staining and Refinishing.

Requirements
Nice to have
• I would like to have the white and grey line like the bottom of my vehicle wrap, Light Grey to match my truck also.

```html
<!DOCTYPE html>
<html lang="en">
<head>
<meta charset="utf-8">
<title>Venter Coatings – Business Card</title>
<link href="https://fonts.googleapis.com/css2?family=Roboto:wght@400;500&display=swap" rel="stylesheet">
<style>
  :root {
    --page-bg: #2b2b2d;
    --card-top: #4a4a4d;
    --card-bottom: #323234;
    --accent: #1ba1e6;
    --accent-deep: #0f7fc4;
    --text-light: #f2f2f2;
  }
  * { box-sizing: border-box; margin: 0; padding: 0; }
  html, body {
    width: 1200px; height: 930px; overflow: hidden;
    background: var(--page-bg);
    font-family: "Roboto", Arial, sans-serif;
  }
  .sheet {
    width: 1200px; height: 930px;
    display: flex; flex-direction: column; align-items: center; justify-content: center;
    gap: 40px;
  }
  .card {
    position: relative;
    width: 720px; height: 411px;
    border-radius: 22px;
    overflow: hidden;
    background: linear-gradient(160deg, var(--card-top), var(--card-bottom));
    box-shadow: 0 14px 30px rgba(0,0,0,.45);
  }
  .card::after {
    content: ""; position: absolute; left: 0; right: 0; bottom: 0; height: 10px;
    background: linear-gradient(90deg, var(--accent), var(--accent-deep));
  }
  .brand { display: flex; align-items: center; gap: 14px; }
  .brand-mark { width: 62px; height: 62px; background: var(--accent); border-radius: 6px; }
  .brand-name {
    color: var(--accent); font-weight: 500; font-size: 40px;
    letter-spacing: 2px; text-transform: uppercase; line-height: 1;
  }

  /* Front: services */
  .card--front { display: flex; flex-direction: column; align-items: center; justify-content: center; gap: 34px; }
  .services { text-align: center; }
  .services-title { color: var(--accent); font-size: 22px; letter-spacing: 1px; margin-bottom: 8px; }
  .services-list { color: var(--text-light); font-size: 17px; line-height: 1.55; }
  .services-list .sep { color: var(--accent); padding: 0 4px; }

  /* Back: contact */
  .card--back { display: flex; align-items: center; padding: 0 50px 0 60px; }
  .card--back .brand-name { font-size: 32px; }
  .card--back .brand-mark { width: 52px; height: 52px; }
  .divider { width: 2px; height: 190px; background: var(--accent); margin: 0 28px; }
  .person-name { color: var(--accent); font-size: 30px; text-transform: uppercase; letter-spacing: 1px; }
  .person-role { color: var(--text-light); font-size: 17px; margin: 4px 0 18px; }
  .contact-list { list-style: none; color: var(--text-light); font-size: 15.5px; }
  .contact-list li { display: flex; align-items: center; gap: 8px; margin-bottom: 6px; }
  .contact-list svg { width: 14px; height: 14px; flex: none; fill: var(--accent); }
</style>
</head>
<body>
<main class="sheet">
  <section class="card card--front">
    <div class="brand">
      <span class="brand-mark"></span>
      <span class="brand-name">Venter Coatings</span>
    </div>
    <div class="services">
      <h2 class="services-title">SERVICES</h2>
      <p class="services-list">
        Custom Paint &amp; Stain<span class="sep">|</span>Interior &amp; Exterior<span class="sep">|</span>Epoxy Coatings / Garage Floors<br>
        Cabinet Refinishing<span class="sep">|</span>Log Staining and Refinishing.
      </p>
    </div>
  </section>

  <section class="card card--back">
    <div class="brand">
      <span class="brand-mark"></span>
      <span class="brand-name">Venter<br>Coatings</span>
    </div>
    <div class="divider"></div>
    <div class="contact">
      <h1 class="person-name">Rodrigo Venter</h1>
      <p class="person-role">Director</p>
      <ul class="contact-list">
        <li><svg viewBox="0 0 24 24" aria-hidden="true"><path d="M6.6 10.8a15 15 0 0 0 6.6 6.6l2.2-2.2a1 1 0 0 1 1-.25 11.4 11.4 0 0 0 3.6.57 1 1 0 0 1 1 1V20a1 1 0 0 1-1 1A17 17 0 0 1 3 4a1 1 0 0 1 1-1h3.5a1 1 0 0 1 1 1c0 1.25.2 2.45.57 3.57a1 1 0 0 1-.25 1z"/></svg>801-437-2910</li>
        <li><svg viewBox="0 0 24 24" aria-hidden="true"><path d="M3 5h18v14H3zm2 2v.5l7 4.5 7-4.5V7zm0 2.8V17h14V9.8l-7 4.5z"/></svg>Ventercoatings.utah@brushmail.net</li>
        <li><svg viewBox="0 0 24 24" aria-hidden="true"><path d="M12 2a10 10 0 1 0 0 20 10 10 0 0 0 0-20zm6.9 9h-3a15 15 0 0 0-1.3-5.6A8 8 0 0 1 18.9 11zM12 4.1c.9 1.3 1.8 3.6 1.9 6.9h-3.8c.1-3.3 1-5.6 1.9-6.9zM9.4 5.4A15 15 0 0 0 8.1 11h-3a8 8 0 0 1 4.3-5.6zM5.1 13h3a15 15 0 0 0 1.3 5.6A8 8 0 0 1 5.1 13zm6.9 6.9c-.9-1.3-1.8-3.6-1.9-6.9h3.8c-.1 3.3-1 5.6-1.9 6.9zm2.6-1.3a15 15 0 0 0 1.3-5.6h3a8 8 0 0 1-4.3 5.6z"/></svg>www.ventercoatings-utah.net</li>
      </ul>
    </div>
  </section>
</main>
</body>
</html>
```